Salad Dressing label for gourmet food business.

We have been producing condiments from traditional recipes for over 50 years. It's time for the Salad Dressing range to have an overhaul. Each one of our ranges (Mustard, Simmer Sauce, Jam, Chocolate Sauce etc) has a unique bottle and label but we would like our branding to be identified across the entire range. We mainly sell to delicatessens, gift stores, hamper businesses, gourmet food stores, tourism destinations, cafes.
www.gablenook.com.au
Target Market(s)
Gourmet food stores, deli, hampers, gift stores
Requirements
Must have
- Label design to fit 250ml dorica bottle.
Foil - Perhaps in border or logo
This is a range of 10 dressings and expanding. Product name, ingredients, NIPS and COO's, the barcode will be overprinted on a thermal printer.
Nice to have
- Serving suggestions
Have elements that tie in with our lines.
Salad Dressings (tall bottle) as per photos attached
We like the Sample Dressings photo attached, Spiced Pear and Ginger. We like the silver foil (but we would like gold) border and in the picture on the label. Perhaps the logo could go here with gold foil? I don't mind the green as it represents fresh salad.
We would like the finished product to represent established quality and authenticity. Product cooked from traditional recipes but would like the look to be relevant to modern times with an interesting, delicious must-try look.
Should not have
- Should not look like a supermarket product.

```html
<!DOCTYPE html>
<html lang="en">
<head>
<meta charset="utf-8">
<title>Balsamic &amp; Pomegranate Dressing Label</title>
<link rel="stylesheet" href="https://fonts.googleapis.com/css2?family=Bodoni+Moda:wght@500;700;900&family=Montserrat:wght@300;400;500&family=Roboto+Condensed:wght@400;700&display=swap">
<style>
  :root {
    --page: #ecebe8;
    --cream: #f3ede1;
    --cream-deep: #ece4d3;
    --ink: #121110;
    --text: #3b3a38;
    --gold-dark: #a9792f;
    --gold: #c99a4c;
    --gold-light: #ecd29a;
    --badge-green: #2f7d3a;
  }
  * { box-sizing: border-box; margin: 0; padding: 0; }
  html, body { width: 1200px; height: 800px; overflow: hidden; background: var(--page); }
  .canvas { position: relative; width: 1200px; height: 800px; }

  .label {
    position: absolute; left: 210px; top: 18px; width: 780px; height: 764px;
    background: linear-gradient(180deg, var(--cream) 0%, var(--cream-deep) 100%);
    box-shadow: 0 6px 18px rgba(0,0,0,0.12);
    color: var(--text);
    font-family: "Montserrat", sans-serif;
  }
  .foil-band {
    position: absolute; left: 0; width: 100%; height: 32px;
    background: linear-gradient(90deg, var(--gold-dark) 0%, var(--gold) 25%, var(--gold-light) 50%, var(--gold) 75%, var(--gold-dark) 100%);
  }
  .foil-band.top { top: 0; }
  .foil-band.bottom { bottom: 0; }

  .brand-mark {
    position: absolute; left: 50%; top: 62px; transform: translateX(-50%);
    display: flex; align-items: center; gap: 10px;
    font-family: "Bodoni Moda", serif; font-weight: 700;
    font-size: 22px; letter-spacing: 5px; color: var(--gold-dark);
    white-space: nowrap;
  }
  .brand-mark .square { width: 14px; height: 14px; background: var(--ink); }

  .title-band {
    position: absolute; left: 0; top: 167px; width: 100%; height: 154px;
    background: var(--ink);
  }
  .title-band .dots {
    position: absolute; left: 0; width: 100%; height: 4px;
    background-image: radial-gradient(circle, var(--gold) 1.6px, transparent 1.8px);
    background-size: 11px 4px;
  }
  .title-band .dots.upper { top: 14px; }
  .title-band .dots.lower { bottom: 14px; }
  .product-name {
    position: absolute; left: 0; top: 30px; width: 100%; text-align: center;
    font-family: "Bodoni Moda", serif; font-weight: 900;
    font-size: 30px; line-height: 35px; letter-spacing: 1.5px; color: var(--gold);
  }
  .band-brand {
    position: absolute; top: 68px; display: flex; align-items: center; gap: 6px;
    font-family: "Bodoni Moda", serif; font-weight: 700;
    font-size: 10px; letter-spacing: 2px; color: var(--gold);
  }
  .band-brand .square { width: 8px; height: 8px; background: var(--gold); }
  .band-brand.left { left: 62px; }
  .band-brand.right { right: 62px; }

  .column { position: absolute; top: 362px; text-align: center; font-size: 11.5px; line-height: 15px; font-weight: 400; }
  .column.ingredients { left: 22px; width: 220px; }
  .column.ingredients p { margin-bottom: 14px; }
  .column.ingredients .heading { font-weight: 500; text-transform: uppercase; }

  .column.story { left: 258px; width: 272px; }
  .tagline {
    font-family: "Bodoni Moda", serif; font-weight: 700;
    font-size: 13px; letter-spacing: 4px; line-height: 20px; text-transform: uppercase; color: var(--ink);
  }
  .serving-title {
    margin: 100px 8px 10px; padding-top: 7px; border-top: 1px solid var(--text);
    font-size: 9.5px; letter-spacing: 2.5px; text-transform: uppercase; font-weight: 500;
  }

  .nutrition {
    position: absolute; left: 550px; top: 365px; width: 212px;
    border: 2px solid var(--ink); background: #fff;
    font-family: "Roboto Condensed", sans-serif; font-size: 9px; color: var(--ink);
    padding: 3px 5px 4px;
  }
  .nutrition h2 {
    font-size: 11px; font-weight: 700; letter-spacing: 1.5px; text-align: center;
    border-bottom: 1px solid var(--ink); padding-bottom: 2px;
  }
  .nutrition .meta { display: flex; justify-content: space-between; padding: 2px 0; border-bottom: 2px solid var(--ink); }
  .nutrition table { width: 100%; border-collapse: collapse; }
  .nutrition th { font-weight: 700; text-align: right; line-height: 11px; padding: 3px 0; border-bottom: 1px solid var(--ink); }
  .nutrition td { line-height: 12px; }
  .nutrition td.num { text-align: right; }
  .nutrition tr.last td { border-top: 1px solid var(--ink); }

  .maker {
    position: absolute; left: 550px; top: 557px; width: 212px; text-align: center;
    font-size: 9px; line-height: 12.5px;
  }
  .maker .name { font-weight: 500; text-transform: uppercase; }
  .maker .web { margin-top: 11px; }

  .origin-badge {
    position: absolute; left: 41px; top: 663px; width: 166px; height: 44px;
    border: 2px solid var(--badge-green); border-radius: 4px; background: #fff;
  }
  .origin-badge .tile { position: absolute; left: 6px; top: 6px; width: 28px; height: 28px; background: var(--badge-green); }

  .origin-line {
    position: absolute; left: 293px; top: 650px; width: 200px; text-align: center;
    font-family: "Bodoni Moda", serif; font-weight: 500;
    font-size: 10px; letter-spacing: 3px; text-transform: uppercase; color: var(--ink);
  }
  .volume {
    position: absolute; left: 370px; top: 676px; width: 46px; height: 20px;
    border: 1px solid var(--ink); border-radius: 50%;
    font-family: "Bodoni Moda", serif; font-size: 8.5px; font-weight: 700;
    display: flex; align-items: center; justify-content: center; color: var(--ink);
  }
</style>
</head>
<body>
<div class="canvas">
  <section class="label">
    <div class="foil-band top"></div>

    <div class="brand-mark"><span class="square"></span>ELDERWICK TREATS</div>

    <div class="title-band">
      <div class="dots upper"></div>
      <div class="band-brand left"><span class="square"></span>ELDERWICK</div>
      <h1 class="product-name">BALSAMIC &amp;<br>POMEGRANATE<br>DRESSING</h1>
      <div class="band-brand right"><span class="square"></span>ELDERWICK</div>
      <div class="dots lower"></div>
    </div>

    <div class="column ingredients">
      <p><span class="heading">Ingredients:</span><br>Balsamic Vinegar,<br>Pomegranate Juice,<br>Brown Sugar, Spice</p>
      <p>Dark thick balsamic vinegar<br>lashed with the sweetness<br>of pomegranate. Elderwick<br>Treats Balsamic</p>
      <p>Warning:<br>This product is addictive.</p>
      <p>Allergen:<br>This product contain &nbsp;Lorem<br>ipsum dolor sit amet,</p>
    </div>

    <div class="column story">
      <p class="tagline">Product cooked from<br>traditional recipes</p>
      <p class="serving-title">Serving Suggestions</p>
      <p>Pomegranate Dressing adds<br>a burst of tart sweetness to<br>salads, meats or seafood.</p>
    </div>

    <div class="nutrition">
      <h2>NUTRITIONAL INFORMATION</h2>
      <div class="meta"><span>Servings per package: 6</span><span>Serving size: 20g</span></div>
      <table>
        <tr><th></th><th></th><th>Average<br>Per Serve</th><th>Average<br>Per 100g</th></tr>
        <tr><td>Energy</td><td></td><td class="num">(304cal) 1272kJ</td><td class="num">(60cal) 254kJ</td></tr>
        <tr><td>Protein</td><td></td><td class="num">0.3g</td><td class="num">0.06g</td></tr>
        <tr><td>Fat</td><td>- Total</td><td class="num">0g</td><td class="num">0g</td></tr>
        <tr><td></td><td>- Saturated</td><td class="num">0g</td><td class="num">0g</td></tr>
        <tr><td>Carbohydrate</td><td>- Total</td><td class="num">82.4g</td><td class="num">16.48g</td></tr>
        <tr><td></td><td>- Sugars</td><td class="num">82.12g</td><td class="num">16.42g</td></tr>
        <tr class="last"><td>Sodium</td><td></td><td class="num">4mg</td><td class="num">0.8mg</td></tr>
      </table>
    </div>

    <div class="maker">
      <p class="name">The Gable Nook</p>
      <p>14 Mill Orchard Road<br>Wattle Vale NSW 2599<br>Australia</p>
      <p class="web">www.gablenook.com.au/</p>
    </div>

    <div class="origin-badge" role="img" aria-label="Country of origin badge"><span class="tile"></span></div>

    <p class="origin-line">Made in Australia</p>
    <div class="volume">250 Ml</div>

    <div class="foil-band bottom"></div>
  </section>
</div>
</body>
</html>
```